Tallowmere Office Solutions needs a new interactive and interesting website

We need an interesting, professional, modern and functional company website for Tallowmere Office Solutions - a young IT Services company based out of Chennai, India.

Tallowmere Office Solutions is a fully owned subsidiary of Hollin Cellarhouse, one of the world's leading direct to consumer wine merchant.

We already have a registered company logo which must feature in the website.

We conceive, design, develop, test, implement and support IT solutions across the entire Hollin Cellarhouse IT landscape. For ex : We currently run about 25 e-commerce websites for Hollin Cellarhouse on QVM and Dot Net.

We would like to see our corporate colors used in the website. (Burgundy wine and wine green - source: www.tallowmereos.example)

We are looking at this website to communicate a fun, friendly and professionally managed company - reaching out to career seekers, prospective customers and general public.

For reference - The company name 'Tallowmere' is an inspiration from the Hollin Cellarhouse lineage.

The second image with the world map is stickered on our main entrance to the office, I am not sure where this can be used -just putting it out there..
Updates

Please note that there are only a few more days to submit designs for this contest  !

I would appreciate if you can help posting your designs in time for our review and consideration.

Thanks.

Project Deadline Extended
Reason: Thanks for your inputs. We have a number of designers and a lot to digest and work with in the past few days. There has been a rush of new designs in the last few days Hence we will require more time to process these and make our decision. Hence i am requesting the contest to be open for more days. Regards, Soren

Target Market(s)

Prospective job seekers who want to know more about the company and also wish to apply for a job vacancy
People wanting to know more about the company in general and our progress
People who want to see what we offer and how we can help them too - prospective customers
Companies that are interested in our IT Captive journey and are looking for a business opportunity

Industry/Entity Type

E-Commerce

Requirements
Must have
• Log In/ Register facility acting as a Single Sign on for Intranet (Employees)

Facility to post job vacancies (with an expiry date) and enable people to apply for a role and upload their CV/Resume.

Facility to Review Job applications

Facility for website visitors to contact Tallowmere office Solutions via an online 'Contact Us' form with a split of job seekers and business opportunities

Gallery facility to upload pictures regarding company events
Nice to have
• Less Cluttered and contemporary design
Some Wine/Vineyard inspirations will be good but not too much, the company is an IT services company

```html
<!DOCTYPE html>
<html lang="en">
<head>
<meta charset="utf-8">
<title>Tallowmere Office Solutions</title>
<link href="https://fonts.googleapis.com/css2?family=Open+Sans:wght@400;600;700&display=swap" rel="stylesheet">
<style>
:root{
  --olive:#8a8c34;
  --olive-dark:#686b24;
  --olive-text:#7d7f22;
  --wine:#8f1d4b;
  --ink:#333;
  --muted:#9a9a9a;
  --line:#e6e6e6;
  --band:#f4f4f4;
}
*{margin:0;padding:0;box-sizing:border-box}
html,body{width:915px;height:1200px;overflow:hidden;background:#fff;font-family:"Open Sans",sans-serif;color:var(--ink)}
.page{position:relative;width:915px;height:1200px}
.abs{position:absolute}

.site-header{left:0;top:0;width:915px;height:65px;background:#f1f1ee;box-shadow:0 1px 3px rgba(0,0,0,.15);z-index:2}
.brand{left:84px;top:8px;display:flex;align-items:center;gap:8px}
.brand-mark{width:22px;height:22px;border-radius:50%;background:var(--wine)}
.brand-name{color:var(--wine);font-weight:700;font-size:20px;line-height:1.05}
.brand-name small{display:block;font-weight:400;font-size:15px}
.main-nav{left:447px;top:0;display:flex;height:65px;font-size:12px}
.main-nav a{color:#333;text-decoration:none;padding:0 12px;line-height:74px}
.main-nav a.active{background:var(--olive);color:#fff;padding:0 10px}

.hero{left:0;top:65px;width:915px;height:417px;background:linear-gradient(100deg,#8d8f92 0%,#c9c6c0 35%,#e9e3da 60%,#b59c86 80%,#4a3a30 100%)}
.hero-caption{left:84px;top:227px;width:348px;height:139px;background:rgba(30,30,30,.72);border-left:4px solid var(--olive);padding:14px 18px;color:#fff}
.hero-caption h1{font-weight:400;font-size:22px;margin-bottom:10px}
.hero-caption p{font-size:11.5px;line-height:14px;color:#e8e8e8}
.hero-dots{left:438px;top:466px;display:flex;gap:2px}
.hero-dots i{width:6px;height:6px;border-radius:50%;background:#bbb;display:block}
.hero-dots i.on{background:#6a9a3a}

.welcome{left:0;top:482px;width:915px;height:56px;background:var(--band);border-bottom:1px solid var(--line)}
.welcome p{position:absolute;left:84px;top:17px;font-size:11.5px}
.welcome p b{font-weight:400;font-size:17px}
.btn{background:linear-gradient(#7c7f28,#5e6119);color:#fff;border:1px solid #4d5014;border-radius:3px;font-family:inherit}
.welcome .btn{position:absolute;left:673px;top:13px;width:106px;height:32px;font-size:14px;font-weight:600}

.feature{top:558px;width:230px}
.feature h2{font-weight:400;font-size:15px;letter-spacing:-.2px;margin-bottom:13px;white-space:nowrap}
.feature .thumb{height:117px}
.feature p{font-size:9.5px;line-height:12px;color:var(--muted);margin-top:13px;width:200px}
.feature a{display:block;font-size:10px;color:var(--olive-text);text-decoration:none;margin-top:6px}
.rule{left:0;top:804px;width:915px;height:1px;background:#f0f0f0}

.panel{top:807px;height:193px;background:var(--olive)}
.panel h3{background:var(--olive-dark);color:#fff;font-weight:400;font-size:15px;height:38px;line-height:38px;padding-left:10px}
.gallery{left:84px;width:354px}
.gallery .slide{position:absolute;top:51px;width:146px;height:132px}
.gallery .arrow{position:absolute;top:82px;color:#fff;font-size:34px;font-weight:300}
.apply{left:448px;width:383px}
.apply h3{padding-left:15px}
.field{position:absolute;color:#fff;font-size:12px}
.field span{display:block;margin-bottom:4px}
.field div{background:#fff;border:1px solid #ccc;width:163px;height:20px}
.apply .btn{position:absolute;left:14px;top:147px;width:78px;height:26px;font-size:11.5px}

.footer-col{top:1020px;width:180px}
.footer-col h4{font-weight:400;font-size:14px;margin-bottom:9px}
.footer-col ul{list-style:none;font-size:9.5px;color:var(--muted)}
.footer-col li{line-height:15.5px}
.footer-col li.current{color:var(--olive-text);font-weight:600}
.footer-col p{font-size:9.5px;color:var(--muted);line-height:17px}
.social li{display:flex;align-items:center;gap:10px;line-height:18.5px}
.social i{width:8px;height:8px;border-radius:50%;background:#ccc;display:block}
.contact{width:200px}
.contact li{display:flex;gap:8px;font-size:8.5px;line-height:11.5px;margin-bottom:12px;white-space:nowrap}
.contact svg{flex:none;margin-top:1px}
.base{left:0;top:1162px;width:915px;height:1px;background:#eee}
.copy{left:83px;top:1176px;font-size:10px}
.legal{left:643px;top:1176px;font-size:9.5px;word-spacing:1px}
.legal span{margin:0 16px}
</style>
</head>
<body>
<div class="page">
  <header class="site-header abs">
    <div class="brand abs"><span class="brand-mark"></span><span class="brand-name">Tallowmere<small>Office Solutions</small></span></div>
    <nav class="main-nav abs">
      <a class="active">Home</a><a>About us</a><a>Clients</a><a>Services</a><a>Careers</a><a>Contact us</a>
    </nav>
  </header>

  <section class="hero abs" role="img" aria-label="Photo of staff working at computers in a bright office"></section>
  <div class="hero-caption abs">
    <h1>Delivering IT Excellence</h1>
    <p>Welcome to Tallowmere Office Solutions, an emerging provider of global IT consulting and software services. We are part of the Hollin Cellarhouse group, a family run business and the world's largest multi-channel home delivery wine merchant.</p>
  </div>
  <div class="hero-dots abs"><i class="on"></i><i></i><i></i><i></i><i></i></div>

  <section class="welcome abs">
    <p><b>Welcome :</b> Welcome to Tallowmere Office Solutions, an emerging provider of global IT.</p>
    <button class="btn">Read more</button>
  </section>

  <article class="feature abs" style="left:84px">
    <h2>Packaged Applications</h2>
    <div class="thumb" role="img" aria-label="Pricing table of packaged plans" style="background:linear-gradient(90deg,#1d2f5a,#2a6fb0 40%,#3aa04a 55%,#2a6fb0 75%,#1d2f5a)"></div>
    <p>Lorem ipsum dolor sit amet, consectetur adipisicing elit, sed do eiusmod tempor incididunt ut labore et dolore magna aliqua...</p>
    <a>Read More</a>
  </article>
  <article class="feature abs" style="left:344px">
    <h2>Enterprise Application Integration</h2>
    <div class="thumb" role="img" aria-label="Grid of colourful application icons" style="background:linear-gradient(135deg,#222,#5a3a2a 30%,#2b4a6a 60%,#1a1a1a)"></div>
    <p>Lorem ipsum dolor sit amet, consectetur adipisicing elit, sed do eiusmod tempor incididunt ut labore et dolore magna aliqua...</p>
    <a>Read More</a>
  </article>
  <article class="feature abs" style="left:603px">
    <h2>Digital Commerce</h2>
    <div class="thumb" role="img" aria-label="Green keyboard key with a shopping cart" style="background:linear-gradient(120deg,#d8d8d8,#9a9a9a 30%,#1fae50 55%,#17883e 80%,#bdbdbd)"></div>
    <p>Lorem ipsum dolor sit amet, consectetur adipisicing elit, sed do eiusmod tempor incididunt ut labore et dolore magna aliqua...</p>
    <a>Read More</a>
  </article>
  <div class="rule abs"></div>

  <section class="panel gallery abs">
    <h3>Our Gallery</h3>
    <span class="arrow" style="left:7px">&#10216;</span>
    <div class="slide" role="img" aria-label="Company event photo of staff at desks" style="left:25px;background:linear-gradient(120deg,#e8e8ea,#b9a08a 55%,#6a7a9a)"></div>
    <div class="slide" role="img" aria-label="Company event photo of a training room" style="left:182px;background:linear-gradient(120deg,#9a8aa0,#c9b9b4 50%,#5a5a60)"></div>
    <span class="arrow" style="left:333px">&#10217;</span>
  </section>

  <section class="panel apply abs">
    <h3>Apply For A Job</h3>
    <label class="field" style="left:14px;top:44px"><span>Your Name &nbsp;*</span><div></div></label>
    <label class="field" style="left:204px;top:44px"><span>Your Address *</span><div></div></label>
    <label class="field" style="left:14px;top:100px"><span>Your Phone Number *</span><div></div></label>
    <label class="field" style="left:202px;top:100px"><span>Your Comment *</span><div style="height:59px"></div></label>
    <button class="btn">Register</button>
  </section>

  <div class="footer-col abs" style="left:84px">
    <h4>Site Links</h4>
    <ul><li class="current">Home</li><li>About us</li><li>Clients</li><li>Services</li><li>Careers</li><li>Contact us</li></ul>
  </div>
  <div class="footer-col abs" style="left:272px">
    <h4>What We Do</h4>
    <p>Lorem ipsum dolor sit amet<br>consectetur adipsicing elit,<br>Sed do euismod tempor<br>incidunt magna aliqua..</p>
  </div>
  <div class="footer-col abs social" style="left:461px">
    <h4>Social Media</h4>
    <ul><li><i></i>Friendloop</li><li><i></i>Chirpline</li><li><i></i>Circleplus</li><li><i></i>Lorem</li><li><i></i>Pinboardly</li></ul>
  </div>
  <div class="footer-col abs contact" style="left:650px">
    <h4>Contact Us</h4>
    <ul>
      <li><svg width="9" height="11" viewBox="0 0 9 11"><path d="M4.5 0a4 4 0 0 0-4 4c0 3 4 7 4 7s4-4 4-7a4 4 0 0 0-4-4z" fill="#ccc"/><circle cx="4.5" cy="4" r="1.5" fill="#fff"/></svg><span>Tallowmere Office Solutions Pvt.<br>Ltd.<br>Level 4, Aldergate Tower<br>Suite 12 Brookmoor Business<br>Park</span></li>
      <li><svg width="10" height="10" viewBox="0 0 10 10"><path d="M2 0l2 2.5-1 1.2a6 6 0 0 0 3.3 3.3l1.2-1L10 8 8.5 10C4 9.5.5 6 0 1.5z" fill="#ccc"/></svg><span>Tel: +00 (00) 5550 1420</span></li>
      <li><svg width="11" height="8" viewBox="0 0 11 8"><rect width="11" height="8" fill="#ccc"/><path d="M0 0l5.5 4.5L11 0" stroke="#fff" fill="none"/></svg><span>Email: contactus@tallowmereos.example</span></li>
    </ul>
  </div>

  <div class="base abs"></div>
  <p class="copy abs">Copyright 2014 © Tallowmere All rights reserved.</p>
  <p class="legal abs">Terms &amp; Conditions<span>|</span>Privacy Policy</p>
</div>
</body>
</html>
```